7 3/4 x 5 1/4 Annual Banquet Invitation

Design an invitation for our Chamber's annual banquet. It will be a single sided invitation 5 1/4" wide by 7 3/4" height that we will print in-house. Our logo is attached. The theme is "Serving Together". I was thinking of an image with two hands coming together in a handshake, perhaps intertwining our logo colors. This is just a thought. I am open for any suggestions! Text for the invitation should be as follows: The Board of Directors and Staff cordially invites you to attend the 64th Yearly Gathering & Micro-Trade Fair - Monday, January 22, 2018. 5:30 p.m. Social, 6:00 p.m. Dinner. Cedarvale Chapel, 4819 Harlan P. Moss Rd S, Larkmoor. Please RSVP by January 18, 2018.

Target Market(s)

This invitation will be printed and mailed to our membership.

Industry/Entity Type

Business Management

Colors
33a6d7
faa54b
0355a3
00a990

Requirements
Must have
• Event info as indentified above.
Nice to have
• Our Logo

```html
<!DOCTYPE html>
<html lang="en">
<head>
<meta charset="utf-8">
<title>Serving Together – Annual Banquet Invitation</title>
<link rel="stylesheet" href="https://fonts.googleapis.com/css2?family=Cinzel:wght@400;500;600&display=swap">
<style>
  :root {
    --page: #ffffff;
    --card-grey: #bcbdbf;
    --panel: #f1f2f2;
    --frame-orange: #f5a94c;
    --quote-orange: #faa54b;
    --sky: #33a6d7;
    --navy: #2b3a97;
    --crowd-light: #c9d3dc;
    --crowd-deep: #54728f;
  }
  * { box-sizing: border-box; margin: 0; padding: 0; }
  html, body {
    width: 1200px; height: 1192px; overflow: hidden;
    background: var(--page);
  }
  .invitation {
    position: absolute; left: 220px; top: 35px;
    width: 760px; height: 1122px;
    background: var(--card-grey);
    overflow: hidden;
  }
  .crowd-artwork {
    position: absolute; left: 0; right: 0; bottom: 0; height: 355px;
    background: linear-gradient(180deg, rgba(201,211,220,0) 0%, var(--crowd-light) 28%, #8fa6bb 60%, var(--crowd-deep) 100%);
  }
  .invite-panel {
    position: absolute; left: 102px; top: 107px;
    width: 556px; height: 751px;
    background: var(--panel);
    border: 1px solid var(--frame-orange);
    display: flex; flex-direction: column; align-items: center;
    font-family: "Cinzel", serif;
    color: var(--navy);
    text-align: center;
  }
  .theme {
    margin-top: 50px;
    font-size: 50px; line-height: 46px;
    color: var(--sky);
    font-weight: 400;
  }
  .theme .mark { color: var(--quote-orange); font-weight: 600; }
  .hosts {
    margin-top: 34px;
    font-size: 17px; line-height: 23px;
    font-weight: 500;
  }
  .event-title {
    margin-top: 8px;
    font-size: 48px; line-height: 47px;
    font-weight: 400;
    letter-spacing: -1px;
  }
  .date-band {
    margin-top: 12px;
    width: 478px;
    border-top: 1.5px solid var(--sky);
    border-bottom: 1.5px solid var(--sky);
    padding: 5px 0 6px;
    font-size: 21px; font-weight: 500;
  }
  .details {
    margin-top: 12px;
    font-size: 17px; line-height: 24px; font-weight: 500;
  }
  .rsvp {
    margin-top: 6px;
    font-size: 17px; font-weight: 500;
  }
  .host-name {
    margin-top: auto; margin-bottom: 26px;
    display: flex; flex-direction: column; align-items: center; gap: 10px;
    font-size: 17px; line-height: 20px; font-weight: 600;
    color: var(--navy);
  }
  .host-name .dot {
    width: 40px; height: 40px; border-radius: 50%;
    background: var(--sky);
  }
</style>
</head>
<body>
  <main class="invitation">
    <div class="crowd-artwork" role="img" aria-label="Paper-cut chain of figures holding hands, in soft blue tones"></div>

    <section class="invite-panel">
      <h1 class="theme"><span class="mark">“</span>Serving<br>Together<span class="mark">”</span></h1>

      <p class="hosts">The Board of Directors and<br>Staff cordially invites you to attend</p>

      <h2 class="event-title">The 64th<br>Yearly Gathering<br>&amp; Micro-Trade<br>Fair.</h2>

      <p class="date-band">Monday, January 22, 2018.</p>

      <p class="details">5:30 p.m. Social, 6:00 p.m.<br>Dinner - Cedarvale Chapel,<br>4819 Harlan P. Moss Rd S, Larkmoor.</p>

      <p class="rsvp">Please RSVP by January 18, 2018.</p>

      <div class="host-name">
        <span class="dot"></span>
        <span>Harborline Chamber<br>of Commerce &amp; Tourism</span>
      </div>
    </section>
  </main>
</body>
</html>
```